New Zealand Export company needs business cards

We need new business cards to match our new logo for a company based in New Zealand who deal specifically with the Pacific Islands. We source, consolidate and ship products out of New Zealand to the Pacific Islands. Will attach our old ones and also new logo.
Would like the Islands we deal with and the areas of work we have access to, to be included on the business cards.

Contact Information for Business Card

T +64 9 571 3048
F +64 9 571 6285
12-18 Kowhai Lane, Drury, 2113
PO Box 814, Drury, Auckland 2247, New Zealand
www.falconfreight.example.nz
E sales@falconfreight.example.nz

Font styles to use
Sans Serif

Colors
85abd2
33a6d7
ffffff

Requirements
Must have
• A company of PWM

```html
<!DOCTYPE html>
<html lang="en">
<head>
<meta charset="utf-8">
<title>Falcon Freight – Business Card</title>
<link href="https://fonts.googleapis.com/css2?family=Lato:wght@400;700&display=swap" rel="stylesheet">
<style>
  :root {
    --page-bg: #b4b4b4;
    --card-blue: #0b57a4;
    --card-faint: #3f68b0;
    --band-faint: #1f5daa;
    --title-blue: #9fdcf5;
    --rule-blue: #33a6d7;
    --soft-text: #85abd2;
    --white: #ffffff;
  }
  * { box-sizing: border-box; margin: 0; padding: 0; }
  html, body { width: 1200px; height: 960px; overflow: hidden; }
  body {
    background: var(--page-bg);
    font-family: "Lato", Arial, sans-serif;
    color: var(--white);
    position: relative;
  }
  .card {
    position: absolute;
    top: 187px;
    width: 344px;
    height: 587px;
    background: var(--card-blue);
    border-radius: 16px;
    overflow: hidden;
  }
  .card--front { left: 219px; }
  .card--back { left: 643px; }

  .pattern-band {
    position: absolute;
    left: 0; right: 0;
    height: 37px;
    background: var(--band-faint);
  }
  .pattern-band--top { top: 0; }
  .pattern-band--bottom { bottom: 0; }

  .backdrop-shape {
    position: absolute;
    z-index: 0;
  }
  .card--front .backdrop-shape {
    left: 0; top: 141px; width: 344px; height: 332px;
    background: linear-gradient(135deg, var(--card-faint) 0%, var(--card-blue) 85%);
  }
  .card--back .backdrop-shape {
    left: 0; top: 390px; width: 344px; height: 100px;
    background: linear-gradient(135deg, var(--card-faint) 0%, var(--card-blue) 90%);
  }

  .brand {
    position: absolute;
    left: 0; right: 0;
    z-index: 1;
    display: flex;
    align-items: center;
    justify-content: center;
    gap: 10px;
    font-weight: 700;
    font-size: 30px;
    letter-spacing: 0.5px;
    color: var(--white);
    white-space: nowrap;
  }
  .brand__square { width: 18px; height: 18px; background: var(--white); }
  .card--front .brand { top: 262px; }
  .card--back .brand { top: 78px; }

  .service-info {
    position: absolute;
    top: 318px; left: 24px; right: 24px;
    z-index: 1;
    text-align: center;
  }
  .service-info__areas {
    font-size: 12px;
    font-weight: 700;
    letter-spacing: 1.5px;
    text-transform: uppercase;
    color: var(--title-blue);
  }
  .service-info__rule {
    width: 60px; height: 1px;
    margin: 9px auto;
    background: var(--rule-blue);
  }
  .service-info__islands {
    font-size: 12px;
    line-height: 18px;
    color: var(--white);
  }

  .company-title {
    position: absolute;
    top: 182px; left: 0; right: 0;
    text-align: center;
    font-weight: 700;
    font-size: 24px;
    color: var(--title-blue);
  }
  .company-rule {
    position: absolute;
    top: 218px; left: 112px;
    width: 120px; height: 1px;
    background: var(--rule-blue);
  }
  .contact-icons {
    position: absolute;
    top: 266px; left: 0; right: 0;
    display: flex;
    justify-content: center;
    gap: 12px;
  }
  .contact-icons svg { width: 16px; height: 16px; display: block; }
  .contact-lines {
    position: absolute;
    top: 289px; left: 0; right: 0;
    text-align: center;
    font-size: 16px;
    line-height: 21.3px;
    z-index: 1;
  }
  .address {
    position: absolute;
    top: 503px; left: 0; right: 0;
    z-index: 1;
    text-align: center;
    font-size: 18px;
    line-height: 18.5px;
    font-style: normal;
  }
</style>
</head>
<body>

  <section class="card card--front">
    <div class="pattern-band pattern-band--top" role="img" aria-label="Repeating brand monogram pattern band"></div>
    <div class="backdrop-shape" role="img" aria-label="Large faint brand monogram backdrop"></div>
    <div class="brand"><span class="brand__square"></span>Falcon Freight</div>
    <div class="service-info">
      <p class="service-info__areas">Source · Consolidate · Ship</p>
      <div class="service-info__rule"></div>
      <p class="service-info__islands">Fiji · Samoa · Tonga · Cook Islands<br>Niue · Vanuatu · Tokelau</p>
    </div>
    <div class="pattern-band pattern-band--bottom" role="img" aria-label="Repeating brand monogram pattern band"></div>
  </section>

  <section class="card card--back">
    <div class="backdrop-shape" role="img" aria-label="Large faint brand monogram backdrop"></div>
    <div class="brand"><span class="brand__square"></span>Falcon Freight</div>

    <h1 class="company-title">Falcon Freight</h1>
    <div class="company-rule"></div>

    <div class="contact-icons">
      <svg viewBox="0 0 16 16" aria-label="Phone"><circle cx="8" cy="8" r="8" fill="#fff"/><path d="M5 4.2l1.5-.4 1 2-1 .8c.5 1.1 1.3 1.9 2.3 2.4l.8-1 2 1-.4 1.5c-3.2.2-6.4-3-6.2-6.3z" fill="#0b57a4"/></svg>
      <svg viewBox="0 0 16 16" aria-label="Fax"><circle cx="8" cy="8" r="8" fill="#fff"/><rect x="5.5" y="3.8" width="5" height="2.5" fill="none" stroke="#0b57a4" stroke-width="1"/><rect x="4" y="6.5" width="8" height="4" rx="0.6" fill="#0b57a4"/><rect x="5.5" y="9.5" width="5" height="3" fill="#fff" stroke="#0b57a4" stroke-width="1"/></svg>
      <svg viewBox="0 0 16 16" aria-label="Email"><circle cx="8" cy="8" r="8" fill="#fff"/><rect x="4" y="5.2" width="8" height="5.6" rx="0.6" fill="#0b57a4"/><path d="M4.3 5.6L8 8.4l3.7-2.8" fill="none" stroke="#fff" stroke-width="0.8"/></svg>
      <svg viewBox="0 0 16 16" aria-label="Website"><circle cx="8" cy="8" r="8" fill="#fff"/><g fill="none" stroke="#0b57a4" stroke-width="0.8"><circle cx="8" cy="8" r="4.5"/><ellipse cx="8" cy="8" rx="2" ry="4.5"/><path d="M3.5 8h9M4.2 5.8h7.6M4.2 10.2h7.6"/></g></svg>
    </div>

    <div class="contact-lines">
      <p>+64 9 571 3048</p>
      <p>+64 9 571 6285</p>
      <p>E sales@falconfreight.example.nz</p>
      <p>www.falconfreight.example.nz</p>
    </div>

    <address class="address">
      <p>12-18 Kowhai Lane, Drury, 2113</p>
      <p>PO Box 814, Drury, Auckland 2247</p>
      <p>New Zealand</p>
    </address>
  </section>

</body>
</html>
```